New Stationery Design Project

We got a project done from you for Pravonix stationary design. We have changed the name of the company from Pravonix to Kelmra.
So we want to redesign our stationay.
We are a VOIP, hosted pbx, and cloud services provider. Clients are mostly hotels, offices, business etc. needing phone services.
Our Slogan is : "Low cost, high quality service"
the logo has to be changed from Pravonix to Kelmra
Business address is
4172 Marrow Pkwy, suite 210
Dallas TX 75399
Phone: 555-013-4872
Fax: 555-013-4872
Website: Kelmra.example
Industry/Entity Type
Business
Look and feel
Each slider illustrates characteristics of the customer's brand and the style your logo design should communicate.

```html
<!DOCTYPE html>
<html lang="en">
<head>
<meta charset="utf-8">
<title>Kelmra Stationery — Business Card</title>
<link rel="stylesheet" href="https://fonts.googleapis.com/css2?family=Barlow:wght@300;400;600;700&display=swap">
<style>
  :root {
    --page-bg: #d9d6d2;
    --card-dark: #262626;
    --card-light: #e8e8e8;
    --ink-dark: #2a2a2a;
    --ink-light: #e9e9e9;
    --ink-muted: #d8d8d8;
    --accent-blue: #1a8fd0;
    --accent-red: #d7263d;
    --band-blue: #1c98d6;
    --band-orange: #e8841f;
    --band-magenta: #d21e7b;
    --band-red: #d5262e;
    --band-black: #1e1e1e;
  }
  * { margin: 0; padding: 0; box-sizing: border-box; }
  html, body { width: 1200px; height: 900px; overflow: hidden; }
  body {
    background: var(--page-bg);
    font-family: "Barlow", "Helvetica Neue", Arial, sans-serif;
    display: flex;
    flex-direction: column;
    align-items: center;
    justify-content: center;
    gap: 40px;
  }
  .card {
    position: relative;
    width: 700px;
    height: 400px;
    overflow: hidden;
    box-shadow: 0 6px 18px rgba(0,0,0,0.18);
  }

  /* Back side */
  .card-back { background: var(--card-dark); color: var(--ink-light); }
  .card-back .brand-mark {
    position: absolute;
    left: 50%; top: 150px;
    transform: translateX(-50%);
    display: flex; align-items: center; gap: 14px;
    font-weight: 700; font-size: 64px; letter-spacing: -1px;
    color: var(--ink-light);
  }
  .brand-dot { width: 22px; height: 22px; border-radius: 50%; background: var(--accent-blue); flex: none; }
  .accent-line { position: absolute; height: 5px; background: var(--accent-blue); }
  .accent-line.top-right { right: 0; top: 44px; width: 70px; }
  .accent-line.bottom-left { left: 0; bottom: 44px; width: 70px; }
  .slogan {
    position: absolute; right: 60px; bottom: 34px;
    font-size: 23px; font-weight: 400; letter-spacing: 0.4px;
    color: var(--ink-muted);
    white-space: nowrap;
  }

  /* Front side */
  .card-front { background: var(--card-light); color: var(--ink-dark); }
  .card-front .brand-mark {
    position: absolute; left: 60px; top: 170px;
    display: flex; align-items: center; gap: 12px;
    font-weight: 700; font-size: 54px; letter-spacing: -1px;
    color: var(--ink-dark);
  }
  .contact-block { position: absolute; left: 420px; top: 60px; }
  .person-name { font-size: 30px; font-weight: 400; letter-spacing: 0.5px; line-height: 1; }
  .person-title { font-size: 14px; margin-top: 6px; }
  .phone-list { list-style: none; margin-top: 34px; font-size: 15px; line-height: 1.35; }
  .phone-list .label { color: var(--accent-blue); font-weight: 600; margin-right: 8px; }
  .address { font-style: normal; font-size: 15px; line-height: 1.35; margin-top: 18px; }
  .website {
    position: absolute; left: 230px; bottom: 74px;
    font-size: 20px; color: var(--accent-red); letter-spacing: 0.3px;
  }
  .pattern-band {
    position: absolute; left: 0; right: 0; bottom: 0; height: 30px;
    background: linear-gradient(90deg,
      var(--band-blue) 0%, var(--band-orange) 22%, var(--band-blue) 42%,
      var(--band-magenta) 62%, var(--band-orange) 80%, var(--band-red) 93%, var(--band-black) 100%);
  }
</style>
</head>
<body>
  <section class="card card-back" aria-label="Business card, back">
    <span class="accent-line top-right"></span>
    <div class="brand-mark"><span class="brand-dot"></span>Kelmra</div>
    <span class="accent-line bottom-left"></span>
    <p class="slogan">Low cost, high quality service</p>
  </section>

  <section class="card card-front" aria-label="Business card, front">
    <div class="brand-mark"><span class="brand-dot"></span>Kelmra</div>
    <div class="contact-block">
      <h1 class="person-name">JOHN DOE</h1>
      <p class="person-title">Managing Partner</p>
      <ul class="phone-list">
        <li><span class="label">T</span>555-013-4872</li>
        <li><span class="label">F</span>555-013-4872</li>
      </ul>
      <address class="address">4172 Marrow Pkwy, suite 210,<br>Dallas TX 75399</address>
    </div>
    <p class="website">kelmra.example</p>
    <div class="pattern-band" role="img" aria-label="Decorative band of coloured speech-bubble pattern"></div>
  </section>
</body>
</html>
```